halden row buisness card design

I need a buisness card that has an orange and red outline a side on antelopes head with long horns.I love the one I found on searchly but it has a watermark see below,would it be possible to have something similar?
There is only one other supplier of skins on the sunshine coast ,very expensive and there are a lot of Australian hides.I can supply
a less expensive choice which is extremly different.

Target Market(s)

home owners family stylists bulk buying anniverary wedding gifts

Industry/Entity Type

Searchly

Contact Information for Business Card

HALDEN ROW
EXOTIC HOMEWARES FOR THE MODERN HOME
MIRANDA 0417263948 bellamoor@examplemail.test
imported from Africa no single product the same

Requirements
Must have
• on front HALDEN ROW large either side of logo
red and orange

ethically produced
Nice to have
• I still have to have more pics of gear set up so just one on back
Should not have
• live animals research shows people dont like to look at animal
no running writing

```html
<!DOCTYPE html>
<html lang="en">
<head>
<meta charset="utf-8">
<title>Halden Row – Business Card</title>
<link rel="stylesheet" href="https://fonts.googleapis.com/css2?family=Encode+Sans+Expanded:wght@600;700&display=swap">
<style>
  :root {
    --page: #ffffff;
    --card-orange: #f9a63a;
    --brand-red: #841b22;
    --mark-light: #f2933a;
    --mark-deep: #d26f30;
  }
  html, body {
    margin: 0;
    padding: 0;
    width: 1000px;
    height: 1200px;
    overflow: hidden;
    background: var(--page);
  }
  .sheet {
    position: relative;
    width: 1000px;
    height: 1200px;
    font-family: "Encode Sans Expanded", "Verdana", sans-serif;
    color: var(--brand-red);
  }
  .card {
    position: absolute;
    left: 59px;
    width: 882px;
    height: 480px;
    background: var(--card-orange);
    overflow: hidden;
  }
  .card--front { top: 68px; }
  .card--back  { top: 651px; }

  .brand-name {
    position: absolute;
    margin: 0;
    font-weight: 700;
    font-size: 86px;
    line-height: 1;
    letter-spacing: -1px;
    white-space: nowrap;
  }
  .tagline {
    position: absolute;
    margin: 0;
    font-weight: 600;
    font-size: 27px;
    line-height: 1;
    white-space: nowrap;
  }
  .mark-area {
    position: absolute;
    background: linear-gradient(160deg, var(--mark-light), var(--mark-deep));
  }

  /* Front */
  .card--front .brand-name { left: 26px; top: 322px; }
  .card--front .tagline    { left: 36px; top: 418px; }
  .card--front .mark-area  { left: 731px; top: 20px; width: 151px; height: 444px; border-radius: 60px 0 0 40px; }

  /* Back */
  .card--back .brand-name { right: 28px; top: 24px; }
  .card--back .tagline    { right: 21px; top: 121px; }
  .card--back .mark-area  { left: 0; top: 22px; width: 146px; height: 416px; border-radius: 0 60px 40px 0; }

  .contact {
    position: absolute;
    right: 28px;
    top: 202px;
    margin: 0;
    text-align: right;
    font-weight: 700;
    font-size: 33px;
    line-height: 54px;
    font-style: normal;
  }
  .contact span { display: block; }

  .footer-line {
    position: absolute;
    left: 46px;
    bottom: 12px;
    margin: 0;
    font-weight: 600;
    font-size: 25px;
    line-height: 1;
    white-space: nowrap;
  }
  .footer-line .separator {
    display: inline-block;
    width: 8px;
    height: 8px;
    margin: 0 6px 4px;
    border-radius: 50%;
    background: var(--brand-red);
    vertical-align: middle;
  }
</style>
</head>
<body>
<main class="sheet">
  <section class="card card--front" aria-label="Card front">
    <h1 class="brand-name">HALDEN ROW</h1>
    <p class="tagline">exotic homewares for the modern home</p>
    <div class="mark-area" role="img" aria-label="Brand mark area"></div>
  </section>

  <section class="card card--back" aria-label="Card back">
    <div class="mark-area" role="img" aria-label="Brand mark area"></div>
    <h2 class="brand-name">HALDEN ROW</h2>
    <p class="tagline">exotic homewares for the modern home</p>
    <address class="contact">
      <span class="contact-name">Miranda</span>
      <span class="contact-phone">417 263 948</span>
      <span class="contact-email">bellamoor@examplemail.test</span>
    </address>
    <p class="footer-line">imported from Africa<span class="separator"></span>no single product the same</p>
  </section>
</main>
</body>
</html>
```